I need three graphics made that will go on walls in a basketball lockerroom

I need three graphics made that will go on a basketball lockerroom wall. Here are the specifics.
Graphic 1 (Size 115" wide by 52" tall, min 150 DPI)
This should be something that displays the acronym for TOLVAR. The main background color should be the teal color attached. Use logos and the other approved colors as needed.
Standards
Intensity
Effort
Grit
Energy
Love
Graphic 2 (Size 88" wide by 52" tall, min 150 DPI)
This one should be on the Navy Blue background color attached
and impactful way say Attitude and Effort
Graphic 3 (Size 100" wide by 18" tall, min 150 DPI)
This goes along the top of the way and needs to say
(THS logo) Stars Lead the Way (Star logo) Tolvar Basketball (THS logo)
All three of these need to feel like they are of the same style. For Graphic #2 I thought something maybe like the attached basketball except use the S Star in the middle and say attitude and effort using the colors .. but I'm open to other ideas

```html
<!DOCTYPE html>
<html lang="en">
<head>
<meta charset="utf-8">
<title>Tolvar Basketball Locker Room Graphics</title>
<link rel="stylesheet" href="https://fonts.googleapis.com/css2?family=Alfa+Slab+One&family=Oswald:wght@600&family=Poppins:wght@600&display=swap">
<style>
  :root {
    --navy: #1a2f5a;
    --navy-deep: #132748;
    --navy-glow: #2a4070;
    --teal: #08858b;
    --teal-bright: #0aa3a6;
    --teal-glow: #3aaeae;
    --white: #ffffff;
    --silver: #c9cacd;
    --silver-light: #f0f0f2;
    --shadow-navy: #1b3556;
    --page: #ffffff;
  }
  html, body {
    margin: 0;
    padding: 0;
    width: 1200px;
    height: 571px;
    overflow: hidden;
    background: var(--page);
  }
  .sheet {
    position: relative;
    width: 1200px;
    height: 571px;
  }
  .panel {
    position: absolute;
    display: block;
  }
  .panel--acronym-oval { left: 22px; top: 21px; width: 571px; height: 259px; }
  .panel--acronym-teal { left: 607px; top: 21px; width: 571px; height: 259px; }
  .panel--attitude-effort { left: 23px; top: 292px; width: 437px; height: 258px; }
  .panel--banner-top { left: 475px; top: 293px; width: 702px; height: 126px; }
  .panel--banner-bottom { left: 475px; top: 424px; width: 702px; height: 126px; }

  .wordmark { font-family: "Alfa Slab One", Georgia, serif; }
  .tagline { font-family: "Oswald", "Arial Narrow", sans-serif; font-weight: 600; fill: var(--white); }
  .arc-word { font-family: "Alfa Slab One", Georgia, serif; fill: var(--white); letter-spacing: 2px; }
  .banner-title { font-family: "Oswald", "Arial Narrow", sans-serif; font-weight: 600; }
  .banner-motto { font-family: "Poppins", Arial, sans-serif; font-weight: 600; letter-spacing: 5px; }
  .mark-name { font-family: "Oswald", "Arial Narrow", sans-serif; font-weight: 600; fill: var(--white); }
</style>
</head>
<body>
<main class="sheet">

  <!-- Graphic 1: acronym on oval -->
  <svg class="panel panel--acronym-oval" viewBox="0 0 571 259" aria-label="TOLVAR acronym graphic">
    <defs>
      <radialGradient id="navyBurst" cx="50%" cy="50%" r="70%">
        <stop offset="0" stop-color="var(--navy-glow)"/>
        <stop offset="1" stop-color="var(--navy)"/>
      </radialGradient>
      <radialGradient id="ovalFill" cx="50%" cy="30%" r="70%">
        <stop offset="0" stop-color="var(--teal-bright)"/>
        <stop offset="1" stop-color="var(--teal)"/>
      </radialGradient>
      <linearGradient id="silverFace" x1="0" y1="0" x2="0" y2="1">
        <stop offset="0" stop-color="var(--silver)"/>
        <stop offset="1" stop-color="var(--silver-light)"/>
      </linearGradient>
    </defs>
    <rect class="panel-bg" width="571" height="259" fill="url(#navyBurst)"/>
    <ellipse class="oval" cx="285" cy="129" rx="264" ry="108" fill="url(#ovalFill)"/>
    <g class="oval-rule" fill="none" stroke="var(--white)" stroke-width="2">
      <path d="M156 33 Q 210 22 270 20"/>
      <path d="M313 20 Q 370 22 419 31"/>
      <path d="M156 226 Q 210 238 266 240"/>
      <path d="M310 240 Q 370 238 419 228"/>
    </g>
    <g class="oval-stars" fill="var(--white)">
      <polygon transform="translate(291 23)" points="0,-11 2.6,-3.6 10.5,-3.4 4.2,1.4 6.5,9 0,4.5 -6.5,9 -4.2,1.4 -10.5,-3.4 -2.6,-3.6"/>
      <polygon transform="translate(288 237)" points="0,-11 2.6,-3.6 10.5,-3.4 4.2,1.4 6.5,9 0,4.5 -6.5,9 -4.2,1.4 -10.5,-3.4 -2.6,-3.6"/>
    </g>
    <g transform="skewX(-8) translate(24 0)">
      <text class="wordmark" x="285" y="172" text-anchor="middle" font-size="118"
            textLength="405" lengthAdjust="spacingAndGlyphs"
            fill="url(#silverFace)" stroke="var(--navy)" stroke-width="9"
            stroke-linejoin="round" paint-order="stroke">TOLVAR</text>
    </g>
    <text class="tagline" x="101" y="200" font-size="18" textLength="369" lengthAdjust="spacingAndGlyphs">TOUGHNESS • OWNERSHIP • LOYALTY • VISION • ATTACK • RESPECT</text>
  </svg>

  <!-- Graphic 1 alternate: teal field -->
  <svg class="panel panel--acronym-teal" viewBox="0 0 571 259" aria-label="TOLVAR acronym graphic on teal">
    <defs>
      <radialGradient id="tealBurst" cx="50%" cy="45%" r="70%">
        <stop offset="0" stop-color="var(--teal-glow)"/>
        <stop offset="1" stop-color="var(--teal)"/>
      </radialGradient>
    </defs>
    <rect class="panel-bg" width="571" height="259" fill="url(#tealBurst)"/>
    <g transform="skewX(-8) translate(24 0)">
      <text class="wordmark" x="290" y="179" text-anchor="middle" font-size="134"
            textLength="490" lengthAdjust="spacingAndGlyphs"
            fill="var(--shadow-navy)">TOLVAR</text>
      <text class="wordmark" x="287" y="174" text-anchor="middle" font-size="134"
            textLength="490" lengthAdjust="spacingAndGlyphs"
            fill="var(--white)">TOLVAR</text>
    </g>
    <text class="tagline" x="83" y="230" font-size="20" textLength="405" lengthAdjust="spacingAndGlyphs">TOUGHNESS • OWNERSHIP • LOYALTY • VISION • ATTACK • RESPECT</text>
    <g class="tagline-stars" fill="var(--white)">
      <polygon transform="translate(59 222) scale(0.95)" points="0,-11 2.6,-3.6 10.5,-3.4 4.2,1.4 6.5,9 0,4.5 -6.5,9 -4.2,1.4 -10.5,-3.4 -2.6,-3.6"/>
      <polygon transform="translate(512 222) scale(0.95)" points="0,-11 2.6,-3.6 10.5,-3.4 4.2,1.4 6.5,9 0,4.5 -6.5,9 -4.2,1.4 -10.5,-3.4 -2.6,-3.6"/>
    </g>
  </svg>

  <!-- Graphic 2: attitude and effort -->
  <svg class="panel panel--attitude-effort" viewBox="0 0 437 258" aria-label="Attitude and Effort graphic">
    <defs>
      <radialGradient id="navyBurstWide" cx="50%" cy="50%" r="70%">
        <stop offset="0" stop-color="var(--navy-glow)"/>
        <stop offset="1" stop-color="var(--navy-deep)"/>
      </radialGradient>
      <path id="arcAttitude" d="M164 209 A96 96 0 0 1 178 43"/>
      <path id="arcEffort" d="M260 43 A96 96 0 0 1 274 209"/>
    </defs>
    <rect class="panel-bg" width="437" height="258" fill="url(#navyBurstWide)"/>
    <circle class="center-ring" cx="219" cy="130" r="84" fill="none" stroke="var(--teal)" stroke-width="10" opacity="0.6"/>
    <g class="frame-arcs" fill="none" stroke="var(--silver)" stroke-width="2.5">
      <path d="M165 36.5 A108 108 0 0 1 273 36.5"/>
      <path d="M273 223.5 A108 108 0 0 1 165 223.5"/>
    </g>
    <text class="arc-word" font-size="27">
      <textPath href="#arcAttitude" startOffset="50%" text-anchor="middle">ATTITUDE</textPath>
    </text>
    <text class="arc-word" font-size="27">
      <textPath href="#arcEffort" startOffset="50%" text-anchor="middle">EFFORT</textPath>
    </text>
    <text class="mark-name" x="219" y="139" text-anchor="middle" font-size="24">TOLVAR</text>
  </svg>

  <!-- Graphic 3: top-of-wall banner -->
  <svg class="panel panel--banner-top" viewBox="0 0 702 126" aria-label="Tolvar Basketball banner">
    <defs>
      <linearGradient id="bannerNavy" x1="0" y1="0" x2="0" y2="1">
        <stop offset="0" stop-color="var(--navy-deep)"/>
        <stop offset="1" stop-color="var(--navy)"/>
      </linearGradient>
    </defs>
    <rect class="panel-bg" width="702" height="126" fill="url(#bannerNavy)"/>
    <g class="school-mark">
      <circle cx="71" cy="63" r="47" fill="none" stroke="var(--silver)" stroke-width="3"/>
      <text class="mark-name" x="71" y="73" text-anchor="middle" font-size="30">THS</text>
    </g>
    <text class="banner-title" x="139" y="70" font-size="50" textLength="425" lengthAdjust="spacingAndGlyphs"><tspan fill="var(--teal)">TOLVAR</tspan> <tspan fill="var(--white)">BASKETBALL</tspan></text>
    <g class="motto-rules" stroke="var(--white)" stroke-width="1.5">
      <line x1="142" y1="88" x2="200" y2="88"/>
      <line x1="503" y1="88" x2="564" y2="88"/>
    </g>
    <text class="banner-motto" x="212" y="95" font-size="18" textLength="279" lengthAdjust="spacingAndGlyphs"><tspan fill="var(--white)">STARS </tspan><tspan fill="var(--teal)">LEAD </tspan><tspan fill="var(--white)">THE WAY</tspan></text>
    <g class="team-mark">
      <circle cx="632" cy="63" r="45" fill="none" stroke="var(--teal)" stroke-width="3"/>
      <text class="mark-name" x="632" y="71" text-anchor="middle" font-size="22">TOLVAR</text>
    </g>
  </svg>

  <svg class="panel panel--banner-bottom" viewBox="0 0 702 126" aria-label="Tolvar Basketball banner">
    <rect class="panel-bg" width="702" height="126" fill="url(#bannerNavy)"/>
    <g class="school-mark">
      <circle cx="71" cy="63" r="47" fill="none" stroke="var(--silver)" stroke-width="3"/>
      <text class="mark-name" x="71" y="73" text-anchor="middle" font-size="30">THS</text>
    </g>
    <text class="banner-title" x="139" y="70" font-size="50" textLength="425" lengthAdjust="spacingAndGlyphs"><tspan fill="var(--teal)">TOLVAR</tspan> <tspan fill="var(--white)">BASKETBALL</tspan></text>
    <g class="motto-rules" stroke="var(--white)" stroke-width="1.5">
      <line x1="142" y1="88" x2="200" y2="88"/>
      <line x1="503" y1="88" x2="564" y2="88"/>
    </g>
    <text class="banner-motto" x="212" y="95" font-size="18" textLength="279" lengthAdjust="spacingAndGlyphs"><tspan fill="var(--white)">STARS </tspan><tspan fill="var(--teal)">LEAD </tspan><tspan fill="var(--white)">THE WAY</tspan></text>
    <g class="team-mark">
      <circle cx="632" cy="63" r="45" fill="none" stroke="var(--teal)" stroke-width="3"/>
      <text class="mark-name" x="632" y="71" text-anchor="middle" font-size="22">TOLVAR</text>
    </g>
  </svg>

</main>
</body>
</html>
```